Stationery Design Project

see attached logo and business card layout, envelopes, letterhead, proposal, and invoice stationery needs to all flow.

Industry/Entity Type

Business

```html
<!DOCTYPE html>
<html lang="en">
<head>
<meta charset="utf-8">
<title>Ridgeline Roadworks Stationery</title>
<link href="https://fonts.googleapis.com/css2?family=Open+Sans:wght@400;600&display=swap" rel="stylesheet">
<style>
  :root {
    --ink: #141414;
    --gold: #f2c230;
    --paper: #ffffff;
    --backdrop: #e8e5e0;
  }
  html, body {
    margin: 0;
    padding: 0;
    overflow: hidden;
  }
  body {
    width: 1200px;
    height: 1200px;
    background: var(--backdrop);
    position: relative;
  }
  .sheet {
    position: absolute;
    box-shadow: 0 10px 24px rgba(0,0,0,0.25);
  }
  .sheet svg {
    display: block;
    width: 100%;
    height: 100%;
  }
  .letterhead {
    left: 57px;
    top: 51px;
    width: 795px;
    height: 1037px;
  }
  .envelope {
    left: 403px;
    top: 401px;
    width: 771px;
    height: 333px;
  }
  .brand {
    position: absolute;
    color: var(--paper);
    font-family: "Open Sans", sans-serif;
    font-weight: 600;
    line-height: 1.15;
    white-space: nowrap;
  }
  .brand-name { display: block; }
  .brand-tagline { display: block; }
  .letterhead .brand {
    right: 44px;
    top: 28px;
    text-align: left;
  }
  .letterhead .brand-name { font-size: 28px; }
  .letterhead .brand-tagline { font-size: 13px; margin-top: 4px; }
  .envelope .brand {
    left: 16px;
    top: 282px;
  }
  .envelope .brand-name { font-size: 15px; }
  .envelope .brand-tagline { font-size: 8px; margin-top: 2px; }
</style>
</head>
<body>

  <section class="sheet letterhead" aria-label="Letterhead">
    <svg viewBox="0 0 464 605" preserveAspectRatio="none">
      <rect class="letterhead-ground" width="464" height="605" fill="var(--ink)"/>
      <path class="header-swoosh" d="M170,62 C300,48 420,68 464,100 L464,122 C430,88 350,60 260,58 C220,58 190,60 170,66 Z" fill="var(--gold)"/>
      <path class="writing-area" d="M0,190 C15,95 120,58 260,60 C360,62 430,85 464,118 L464,492 C360,545 160,565 0,555 Z" fill="var(--paper)"/>
      <path class="footer-swoosh" d="M0,555 C160,565 360,545 464,492 L464,500 C360,556 170,574 0,566 Z" fill="var(--gold)"/>
    </svg>
    <div class="brand">
      <span class="brand-name">Ridgeline Roadworks</span>
      <span class="brand-tagline">Roads Built With Care</span>
    </div>
  </section>

  <section class="sheet envelope" aria-label="Envelope">
    <svg viewBox="0 0 450 194" preserveAspectRatio="none">
      <rect class="envelope-ground" width="450" height="194" fill="var(--paper)"/>
      <path class="corner-band" d="M330,0 C390,4 432,26 450,58 L450,0 Z" fill="var(--ink)"/>
      <path class="corner-swoosh" d="M330,0 C390,4 432,26 450,58 L450,64 C428,32 388,8 330,2 Z" fill="var(--gold)"/>
      <path class="base-band" d="M0,120 C120,148 300,172 450,194 L0,194 Z" fill="var(--ink)"/>
      <path class="base-swoosh" d="M200,160 C300,176 380,186 450,194 L410,194 C340,185 270,175 200,160 Z" fill="var(--gold)"/>
    </svg>
    <div class="brand">
      <span class="brand-name">Ridgeline Roadworks</span>
      <span class="brand-tagline">Roads Built With Care</span>
    </div>
  </section>

</body>
</html>
```